Pawn & Gun store business card design

Hello! We would like a new business card design for our pawn & gun store. We loan money on items of value and sell firearms, jewelry, electronics & more.

Card will need to have the following information:

Business name - Prairie Nickel Pawn & Gun
Address - 2417 Hwy 41 S. Suite B Cedar Hollow, TX 75061
Employees name - Marcus Pellen
Phone number - 940-555-0183
Email - PrairieNickelPawn@mailhaven.example
Website - PrairieNickelPawn.example

Somewhere on the card we would like it to say "Offering 10 Month Layaway!" & "We buy & loan on anything of value!". Our main store color is orange (please see logo). Logo does not have to be on the business card but it can be. Would like the back to have an area to write a note on the back. We like vintage things like old coins, collectables, firearms and more so think about this in the design. We want a business card as unique as our store!

Colors

Designer to choose colors to be used in the design.

Requirements
Nice to have
• Vintage Style

```html
<!DOCTYPE html>
<html lang="en">
<head>
<meta charset="utf-8">
<title>Prairie Nickel Pawn &amp; Gun – Business Card</title>
<link rel="stylesheet" href="https://fonts.googleapis.com/css2?family=Lato:wght@400&family=Tinos:wght@400;700&display=swap">
<style>
  :root {
    --page-bg: #3a3532;
    --card-bg: #ffffff;
    --brown: #3b2314;
    --ink: #3d3d3d;
    --orange: #e0661f;
    --rule: #c9c4bf;
  }
  * { box-sizing: border-box; margin: 0; padding: 0; }
  html, body { width: 1200px; height: 844px; overflow: hidden; }
  body {
    background: var(--page-bg);
    position: relative;
    font-family: "Lato", Arial, sans-serif;
  }
  .card {
    position: absolute;
    top: 272px;
    width: 520px;
    height: 300px;
    background: var(--card-bg);
    box-shadow: 0 6px 18px rgba(0,0,0,0.35);
    overflow: hidden;
  }
  .card--front { left: 50px; }
  .card--back { left: 630px; }

  .brand {
    font-family: "Tinos", "Times New Roman", serif;
    font-weight: 700;
    color: var(--orange);
    display: flex;
    align-items: center;
    gap: 8px;
    white-space: nowrap;
  }
  .brand__mark { width: 12px; height: 12px; background: var(--orange); flex: none; }

  .card--front .brand {
    position: absolute;
    top: 48px;
    right: 30px;
    font-size: 22px;
    line-height: 1.1;
  }
  .address {
    position: absolute;
    top: 116px;
    right: 30px;
    text-align: right;
    font-size: 13px;
    line-height: 1.35;
    color: var(--ink);
  }
  .person {
    position: absolute;
    left: 30px;
    top: 150px;
    font-family: "Tinos", "Times New Roman", serif;
    font-weight: 400;
    font-size: 21px;
    letter-spacing: 0.5px;
    color: var(--brown);
    text-transform: uppercase;
  }
  .contacts {
    position: absolute;
    left: 30px;
    top: 186px;
    list-style: none;
    font-size: 14px;
    color: var(--ink);
  }
  .contacts li { display: flex; align-items: center; gap: 7px; height: 21px; }
  .contacts svg { width: 11px; height: 11px; fill: var(--brown); flex: none; }
  .divider {
    position: absolute;
    left: 30px;
    right: 30px;
    top: 254px;
    border-top: 1px solid var(--rule);
  }
  .slogans {
    position: absolute;
    left: 30px;
    right: 30px;
    top: 260px;
    display: flex;
    justify-content: space-between;
    font-family: "Tinos", "Times New Roman", serif;
    font-weight: 700;
    font-size: 15px;
    color: var(--orange);
  }

  .back-band {
    position: absolute;
    left: 0;
    right: 0;
    top: 66px;
    height: 7px;
    background: var(--brown);
  }
  .card--back .brand {
    position: absolute;
    top: 52px;
    left: 50%;
    transform: translateX(-50%);
    background: var(--card-bg);
    padding: 6px 14px;
    font-size: 18px;
  }
</style>
</head>
<body>
  <section class="card card--front">
    <div class="brand"><span class="brand__mark"></span><span>Prairie Nickel Pawn &amp; Gun</span></div>
    <p class="address">2417 Hwy 41 S.<br>Suite B Cedar Hollow<br>TX 75061</p>
    <h1 class="person">Marcus Pellen</h1>
    <ul class="contacts">
      <li><svg viewBox="0 0 12 12"><path d="M2 1h3l1 3-1.5 1a7 7 0 0 0 3 3L9 6.5l3 1v3L11 11C5 11 1 7 1 2z"/></svg>940-555-0183</li>
      <li><svg viewBox="0 0 12 12"><path d="M0 2h12v8H0z M1 3l5 4 5-4" fill="none" stroke="#3b2314" stroke-width="1.4"/></svg>PrairieNickelPawn@mailhaven.example</li>
      <li><svg viewBox="0 0 12 12"><circle cx="6" cy="6" r="6"/></svg>PrairieNickelPawn.example</li>
    </ul>
    <div class="divider"></div>
    <p class="slogans"><span>Offering 10 Month Layaway!</span><span>We buy &amp; loan on anything of value!</span></p>
  </section>

  <section class="card card--back">
    <div class="back-band"></div>
    <div class="brand"><span class="brand__mark"></span><span>Prairie Nickel Pawn &amp; Gun</span></div>
  </section>
</body>
</html>
```